Design interface for an invoicing software

We are developing a new invoicing software that is a very boring topic. Users can use the software to write invoices and manage their income. Therefore we want to inspire the users with a great desgin. By this we mean, for example, the use of photos in the background (streets in New York, landscapes), or "crazy" looking headlines or something else. Target group are young start-ups, freelancers, hairdressers and taxi drivers at the age of 18-40 years. It would also be worth considering to adapt the look to the user's industry. However, the menu items themselves and the approximate position of the information are given. See file "startpoint" What kind of ideas do you have?

Target Market(s)

Europe

Industry/Entity Type

Small Business

Colors

Designer to choose colors to be used in the design.

Requirements
Must have
• the menu items themselves and the approximate position of the information are given. The navigation menu itself can be different.
Should not have
• boring look and feel

```html
<!DOCTYPE html>
<html lang="en">
<head>
<meta charset="utf-8">
<title>Invoicing Dashboard</title>
<link href="https://fonts.googleapis.com/css2?family=Montserrat:wght@700&family=Lato:wght@400;700&display=swap" rel="stylesheet">
<style>
  :root {
    --bg-dark: #1c1d1f;
    --bg-mid: #33343a;
    --text: #ffffff;
    --muted: #8d8f93;
    --accent: #19e6c1;
    --negative: #ee1a6a;
    --positive: #1ee67e;
    --dot-today: #1ecdf0;
    --dot-tomorrow: #f59a0c;
    --legend-expenses: #1bea7a;
    --legend-income: #f014b4;
  }
  * { box-sizing: border-box; margin: 0; padding: 0; }
  html, body { width: 1200px; height: 675px; overflow: hidden; background: var(--bg-dark); }
  body { font-family: 'Lato', sans-serif; color: var(--text); }
  .app { position: relative; width: 1200px; height: 675px; overflow: hidden; }
  .backdrop {
    position: absolute; inset: 0;
    background:
      radial-gradient(ellipse at 50% 55%, #4a4b50 0%, transparent 45%),
      linear-gradient(180deg, #3a3b40 0%, #2a2b2f 45%, #26272a 75%, #303134 100%);
  }
  .abs { position: absolute; }

  .window-controls svg { position: absolute; }

  .menu-toggle { left: 61px; top: 65px; width: 25px; height: 19px; }
  .nav { left: 0; top: 0; }
  .nav-item { position: absolute; left: 0; display: flex; align-items: center; }
  .nav-icon { position: absolute; left: 62px; width: 26px; height: 26px; transform: translateY(-50%); }
  .nav-label { position: absolute; left: 121px; transform: translateY(-50%); font-size: 13.5px; font-weight: 700; color: var(--muted); white-space: nowrap; }
  .nav-item.is-active .nav-label { color: var(--accent); font-size: 17px; font-weight: 400; }

  .heading { font-family: 'Montserrat', sans-serif; font-weight: 700; line-height: 1; white-space: nowrap; }
  .invoices-title { left: 328px; top: 156px; font-size: 42px; }
  .invoices-rule { left: 328px; top: 221px; width: 2px; height: 198px; background: var(--text); }
  .invoice { position: absolute; left: 368px; width: 525px; height: 44px; }
  .invoice-client { position: absolute; left: 0; top: 0; font-size: 16px; font-weight: 700; }
  .invoice-date { position: absolute; left: 0; top: 24px; font-size: 13.5px; }
  .invoice-amount { position: absolute; right: 0; top: -4px; font-size: 20px; }
  .invoice-amount sup { font-size: 10px; vertical-align: 9px; margin-right: 1px; }
  .invoice-amount.is-negative { color: var(--negative); }
  .invoice-amount.is-positive { color: var(--positive); }
  .invoice-due { position: absolute; right: 0; top: 24px; font-size: 13.5px; font-weight: 700; }

  .stats-title { left: 328px; top: 533px; font-size: 44px; }
  .legend { top: 554px; display: flex; align-items: center; font-size: 15px; font-weight: 700; }
  .legend-swatch { width: 9px; height: 9px; margin-right: 8px; }
  .tabs { top: 595px; font-size: 11px; font-weight: 700; letter-spacing: 1px; color: var(--muted); }
  .tab.is-active { color: var(--text); }

  .todo-title { left: 980px; top: 156px; font-size: 42px; }
  .todo-add { left: 1152px; top: 165px; width: 27px; height: 27px; }
  .todo-rule { left: 988px; top: 221px; width: 2px; height: 130px; background: var(--text); }
  .todo-day { left: 1027px; font-size: 11px; font-weight: 700; letter-spacing: 1px; color: var(--muted); }
  .todo-time { left: 1027px; font-size: 14px; font-weight: 700; transform: translateY(-50%); }
  .todo-dot { left: 1084px; width: 7px; height: 7px; border-radius: 50%; transform: translateY(-50%); }
  .todo-dot.is-today { background: var(--dot-today); }
  .todo-dot.is-tomorrow { background: var(--dot-tomorrow); }
  .todo-link { left: 1087px; width: 1px; height: 18px; background: var(--text); opacity: .8; }
  .todo-text { left: 1111px; font-size: 13.5px; white-space: nowrap; transform: translateY(-50%); }
</style>
</head>
<body>
<div class="app">
  <div class="backdrop" role="img" aria-label="Dimmed background photo of a busy New York street with yellow taxis and tall buildings"></div>

  <div class="window-controls">
    <svg style="left:1073px;top:26px" width="20" height="14" viewBox="0 0 20 14"><line x1="1" y1="12" x2="19" y2="12" stroke="#fff" stroke-width="2"/></svg>
    <svg style="left:1117px;top:22px" width="18" height="16" viewBox="0 0 18 16"><rect x="1.5" y="1.5" width="15" height="13" fill="none" stroke="#fff" stroke-width="2.5"/></svg>
    <svg style="left:1159px;top:22px" width="16" height="16" viewBox="0 0 16 16"><path d="M1 1L15 15M15 1L1 15" stroke="#fff" stroke-width="2"/></svg>
  </div>

  <svg class="abs menu-toggle" viewBox="0 0 25 19"><path d="M0 1.5H25M0 9.5H25M0 17.5H25" stroke="#fff" stroke-width="2"/></svg>

  <nav class="nav abs">
    <div class="nav-item is-active" style="top:173px">
      <svg class="nav-icon" viewBox="0 0 26 26"><rect x="3" y="3" width="8" height="11" fill="#19e6c1"/><rect x="13" y="3" width="9" height="7" fill="#19e6c1"/><rect x="3" y="16" width="8" height="6" fill="#19e6c1"/><rect x="13" y="12" width="9" height="10" fill="#19e6c1"/></svg>
      <span class="nav-label">Dashboard</span>
    </div>
    <div class="nav-item" style="top:237px">
      <svg class="nav-icon" viewBox="0 0 26 26" fill="none" stroke="#8d8f93" stroke-width="1.3"><path d="M6 3h14v20H4V6z"/><path d="M8 8h9M8 12h9M8 16h9M8 19h6"/></svg>
      <span class="nav-label">Invoices</span>
    </div>
    <div class="nav-item" style="top:299px">
      <svg class="nav-icon" viewBox="0 0 26 26" fill="none" stroke="#8d8f93" stroke-width="1.3"><path d="M2 4h4l3 13h13l2-9H7"/><circle cx="10" cy="21" r="1.8"/><circle cx="20" cy="21" r="1.8"/></svg>
      <span class="nav-label">Products</span>
    </div>
    <div class="nav-item" style="top:361px">
      <svg class="nav-icon" viewBox="0 0 26 26" fill="none" stroke="#8d8f93" stroke-width="1.3"><circle cx="13" cy="9" r="5.5"/><path d="M3 24c0-6 4.5-9 10-9s10 3 10 9"/></svg>
      <span class="nav-label">Contacts</span>
    </div>
    <div class="nav-item" style="top:424px">
      <svg class="nav-icon" viewBox="0 0 26 26" fill="none" stroke="#8d8f93" stroke-width="1.3"><path d="M3 6l10-3 10 3v2H3z"/><path d="M6 9v11M10 9v11M16 9v11M20 9v11M3 21h20M2 24h22"/></svg>
      <span class="nav-label">Banking</span>
    </div>
    <div class="nav-item" style="top:486px">
      <svg class="nav-icon" viewBox="0 0 26 26" fill="none" stroke="#8d8f93" stroke-width="1.3"><circle cx="13" cy="13" r="11"/><path d="M16.5 9c-1-1.5-6-2-6 1s6 2 6 5-5 2.8-6.5 1M13 6v14"/></svg>
      <span class="nav-label">Expenses</span>
    </div>
    <div class="nav-item" style="top:549px">
      <svg class="nav-icon" viewBox="0 0 26 26" fill="none" stroke="#8d8f93" stroke-width="1.3"><path d="M3 23h21M5 23v-4M9 23v-6M13 23v-8M17 23v-10M21 23v-12M4 15l6-4 5 2 8-8M19 5h4v4"/></svg>
      <span class="nav-label">Reports</span>
    </div>
  </nav>

  <h1 class="heading abs invoices-title">Invoices</h1>
  <div class="abs invoices-rule"></div>
  <section class="invoice-list">
    <div class="invoice" style="top:230px">
      <span class="invoice-client">Nora Lindqvist</span><span class="invoice-date">17/29/2018</span>
      <span class="invoice-amount"><sup>$</sup>246</span><span class="invoice-due">Due on Sept 25, 2018</span>
    </div>
    <div class="invoice" style="top:301px">
      <span class="invoice-client">Marco Felden</span><span class="invoice-date">17/29/2018</span>
      <span class="invoice-amount is-negative"><sup>$</sup>127.80</span><span class="invoice-due">Due on Sept 25, 2018</span>
    </div>
    <div class="invoice" style="top:372px">
      <span class="invoice-client">Elias Brandt</span><span class="invoice-date">17/29/2018</span>
      <span class="invoice-amount is-positive"><sup>$</sup>56.05</span><span class="invoice-due">Due on Sept 25, 2018</span>
    </div>
    <div class="invoice" style="top:444px">
      <span class="invoice-client">Lena Wittmer</span><span class="invoice-date">17/29/2018</span>
      <span class="invoice-amount"><sup>$</sup>246</span><span class="invoice-due">Due on Sept 25, 2018</span>
    </div>
  </section>

  <h2 class="heading abs stats-title">Statistics</h2>
  <div class="abs legend" style="left:695px"><span class="legend-swatch" style="background:var(--legend-expenses)"></span>Expenses</div>
  <div class="abs legend" style="left:818px"><span class="legend-swatch" style="background:var(--legend-income)"></span>Income</div>
  <span class="abs tabs tab is-active" style="left:328px">YEAR</span>
  <span class="abs tabs tab" style="left:416px">MONTH</span>
  <span class="abs tabs tab" style="left:517px">WEEK</span>

  <h2 class="heading abs todo-title">To - do</h2>
  <svg class="abs todo-add" viewBox="0 0 27 27" fill="none" stroke="#fff" stroke-width="1.6"><circle cx="13.5" cy="13.5" r="12.5"/><path d="M13.5 8v11M8 13.5h11"/></svg>
  <div class="abs todo-rule"></div>

  <span class="abs todo-day" style="top:226px">TODAY</span>
  <span class="abs todo-time" style="top:270px">14:20</span>
  <span class="abs todo-dot is-today" style="top:270px"></span>
  <span class="abs todo-text" style="top:270px">Yoga class with Mira</span>
  <span class="abs todo-link" style="top:283px"></span>
  <span class="abs todo-time" style="top:315px">16:40</span>
  <span class="abs todo-dot is-today" style="top:315px"></span>
  <span class="abs todo-text" style="top:315px">Yoga class with Mira</span>
  <span class="abs todo-link" style="top:328px"></span>
  <span class="abs todo-time" style="top:360px">16:40</span>
  <span class="abs todo-dot is-today" style="top:360px"></span>
  <span class="abs todo-text" style="top:360px">Webinar with Luca</span>

  <span class="abs todo-day" style="top:420px">TOMMOROW</span>
  <span class="abs todo-time" style="top:458px">16:40</span>
  <span class="abs todo-dot is-tomorrow" style="top:458px"></span>
  <span class="abs todo-text" style="top:458px">Appointment with</span>
</div>
</body>
</html>
```